stationary for home builder
Birchwood Custom Homes, Inc.
Project: stationary for home builder
stationary for home builder - Real Estate
Creative Brief
Professional
Dale Morrow
President
4200 Tern Avenue, suite 310 Seabright Cove, CA 90000
bchdalemorrow@mailvista.test

```html
<!DOCTYPE html>
<html lang="en">
<head>
<meta charset="utf-8">
<title>Birchwood Custom Homes, Inc. — Business Cards</title>
<link rel="stylesheet" href="https://fonts.googleapis.com/css2?family=Cinzel:wght@400;600;700&display=swap">
<style>
  :root {
    --canvas: #d9d9d9;
    --brand-red: #c0302c;
    --brand-red-dark: #9e2320;
    --brand-red-light: #d8443d;
    --paper: #ffffff;
    --swoosh-grey: #b9b9b9;
    --ink-white: #ffffff;
    --logo-red: #b3231f;
  }
  * { margin: 0; padding: 0; box-sizing: border-box; }
  html, body {
    width: 1200px; height: 895px; overflow: hidden;
    background: var(--canvas);
    font-family: "Cinzel", serif;
  }
  .card-set {
    position: absolute; inset: 0;
    display: flex; align-items: center; justify-content: center; gap: 40px;
  }
  .card {
    position: relative; width: 540px; height: 309px; overflow: hidden;
    box-shadow: 0 4px 14px rgba(0,0,0,.18);
  }
  /* Front */
  .card-front { background: var(--paper); }
  .card-front .front-shape { position: absolute; inset: 0; }
  .holder {
    position: absolute; left: 30px; top: 26px; color: var(--ink-white);
  }
  .holder-name { font-size: 17px; font-weight: 600; letter-spacing: .5px; font-variant: small-caps; }
  .holder-title { font-size: 10px; letter-spacing: 1px; margin-top: 2px; font-variant: small-caps; }
  .contact-list {
    position: absolute; left: 30px; top: 118px; list-style: none; color: var(--ink-white);
    font-size: 10.5px; letter-spacing: .3px; font-variant: small-caps;
  }
  .contact-list li { display: flex; align-items: center; gap: 8px; height: 20px; white-space: nowrap; }
  .contact-icon {
    width: 13px; height: 13px; border-radius: 50%; background: var(--ink-white);
    display: flex; align-items: center; justify-content: center; flex: none;
  }
  .contact-icon svg { width: 9px; height: 9px; }
  .company-mark {
    position: absolute; left: 300px; top: 118px; width: 220px; text-align: center;
    color: var(--logo-red); font-weight: 700;
  }
  .company-mark .mark-square {
    display: block; width: 34px; height: 34px; margin: 0 auto 10px; background: var(--logo-red);
  }
  .company-mark .mark-name { font-size: 30px; line-height: 1; letter-spacing: 1px; }
  .company-mark .mark-sub { font-size: 14px; letter-spacing: 1px; margin-top: 4px; }
  /* Back */
  .card-back {
    background: radial-gradient(ellipse at 45% 40%, var(--brand-red-light), var(--brand-red) 55%, var(--brand-red-dark));
  }
  .back-domain {
    position: absolute; left: 30px; top: 32px; color: var(--ink-white);
    font-size: 16px; letter-spacing: 1px; font-variant: small-caps;
  }
  .house-artwork {
    position: absolute; right: 0; top: 0; width: 240px; height: 309px;
    background: linear-gradient(160deg, rgba(255,255,255,.16), rgba(255,255,255,.04));
  }
</style>
</head>
<body>
<main class="card-set">
  <section class="card card-front" aria-label="Business card front">
    <svg class="front-shape" viewBox="0 0 540 309" preserveAspectRatio="none" aria-hidden="true">
      <rect width="540" height="309" fill="var(--brand-red)"/>
      <path d="M318 0 C248 90 300 210 228 309 L540 309 L540 0 Z" fill="var(--paper)"/>
      <path d="M318 0 C248 90 300 210 228 309" fill="none" stroke="var(--swoosh-grey)" stroke-width="6"/>
    </svg>
    <div class="holder">
      <div class="holder-name">Dale Morrow</div>
      <div class="holder-title">President</div>
    </div>
    <ul class="contact-list">
      <li><span class="contact-icon"><svg viewBox="0 0 10 10"><path d="M5 1a3 3 0 0 0-3 3c0 2.2 3 5 3 5s3-2.8 3-5a3 3 0 0 0-3-3z" fill="var(--brand-red)"/></svg></span>4200 Tern Avenue, suite 310</li>
      <li><span class="contact-icon"></span>Seabright Cove, CA 90000</li>
      <li><span class="contact-icon"><svg viewBox="0 0 10 10"><path d="M2 1l2 1-1 2 3 3 2-1 1 2-2 1C4 9 1 6 1 3z" fill="var(--brand-red)"/></svg></span>555-010-4250</li>
      <li><span class="contact-icon"><svg viewBox="0 0 10 10"><rect x="2" y="3" width="6" height="5" fill="var(--brand-red)"/></svg></span>555-010-7186</li>
      <li><span class="contact-icon"><svg viewBox="0 0 10 10"><rect x="1.5" y="2.5" width="7" height="5" fill="none" stroke="var(--brand-red)"/><path d="M1.5 2.5L5 5.5 8.5 2.5" fill="none" stroke="var(--brand-red)"/></svg></span>bchdalemorrow@mailvista.test</li>
      <li><span class="contact-icon"><svg viewBox="0 0 10 10"><circle cx="5" cy="5" r="3.5" fill="none" stroke="var(--brand-red)"/></svg></span>www.BirchwoodHomes.test</li>
    </ul>
    <div class="company-mark">
      <span class="mark-square"></span>
      <div class="mark-name">BIRCHWOOD</div>
      <div class="mark-sub">CUSTOM HOMES, INC.</div>
    </div>
  </section>

  <section class="card card-back" aria-label="Business card back">
    <div class="back-domain">www.BirchwoodHomes.test</div>
    <div class="house-artwork" role="img" aria-label="Embossed house roofline with windows artwork"></div>
  </section>
</main>
</body>
</html>
```